Etiketten für  Beauty Vitaminreihe
Etiketten für Beauty Vitaminreihe
Zielgruppe
Wir sind eine Lifestyle Firma in Israel die Vitamine für die innere Schönheit produzieren. Unsere Zielgruppe sind Frauen mittleren Alters die sehr auf Ihr Äußeres wert legen.
Aufgabenstellung
Es sind 5 Arten von Vitamin Gummibärchen für die folgenden Vorteile sorgen:
1. Hair Skin and Nails Vitamine ( mit Biotin)
2. Kollagen (anti aging booster)
3. Multivitamin für Frauen
4. Multivitamin für Männer
5. Kurkuma und Ingwer
Genaue Aufteilung des Stickers und was draufstehen muss, wird in einem Word Dokument angehängt. Jede Art hat eine andere Farbe des Deckels, diese werden auch angehängt als Fotos.
Die Rückseite des Etiketts wird mit dem Gewinner fertiggestellt.
Das Design soll sehr simpel und minimalistisch und luxuriös sein, mit einem Hauch von Hotstamping Gold (Rahmen des Logos) und vielleicht noch ein weiteres kleines goldenes Detail.
Die Farben jedes Stickers sollte eine Pastellfarbe haben, in der Farbe des Deckels. Die Farben sollten sehr leicht und hell sein.
Die Maße der Flasche sind: Umfang 20 cm und Höhe 9 cm (von Ecke zu Ecke).
Ich hänge weitere Designs zur Inspiration an, die mir gefallen.

```html
<!DOCTYPE html>
<html lang="en">
<head>
<meta charset="utf-8">
<title>Ovela Vitamin Gummies – Label Series</title>
<link rel="stylesheet" href="https://fonts.googleapis.com/css2?family=Josefin+Sans:wght@400;600&display=swap">
<style>
  :root {
    --paper: #ffffff;
    --ink: #1c1c1c;
    --ink-soft: #3a3a3a;
    --gold: #b8925a;
    --edge: #e4e4e6;

    --pink-cap: #f07ad6;
    --pink-mark: #d36aa8;
    --pink-tint: #f8e6f3;
    --pink-muted: #cdb3c4;

    --plum-cap: #b02595;
    --plum-mark: #9c3189;
    --plum-tint: #f6e3f3;
    --plum-muted: #d7bfd2;

    --amber-cap: #f39a1c;
    --amber-mark: #eca127;
    --amber-tint: #fdf5e3;
    --amber-muted: #e6d9bf;

    --sky-cap: #22a2dc;
    --sky-mark: #2f9fd9;
    --sky-tint: #e3f5fb;
    --sky-muted: #c6e0ec;

    --teal-cap: #2a9284;
    --teal-mark: #3b8a86;
    --teal-tint: #e6f5f4;
    --teal-muted: #cbe0dd;
  }
  * { box-sizing: border-box; margin: 0; padding: 0; }
  html, body { width: 1200px; height: 1200px; overflow: hidden; background: var(--paper); }
  body { font-family: "Josefin Sans", "Century Gothic", sans-serif; color: var(--ink); }

  .lineup { position: relative; width: 1200px; height: 1200px; }

  /* jar geometry, all in em of the jar's own scale */
  .jar { position: absolute; width: 29em; height: 50.6em; }
  .jar__cap {
    position: absolute; left: 0.3em; right: 0.3em; top: 0; height: 8.8em;
    border-radius: 1.4em 1.4em 0.9em 0.9em;
    background: var(--cap);
  }
  .jar__body {
    position: absolute; left: 0; right: 0; top: 7.8em; bottom: 0;
    background: var(--paper);
    border: 1px solid var(--edge);
    border-radius: 3em 3em 4.5em 4.5em;
  }

  .label__tint-block {
    position: absolute; left: 15.5em; top: 14.7em; width: 11.3em; height: 13.9em;
    background: linear-gradient(135deg, var(--tint), #ffffff);
  }
  .label__muted-block {
    position: absolute; left: 0.6em; top: 26.1em; width: 6.7em; height: 10.8em;
    background: var(--muted);
  }
  .label__brand {
    position: absolute; left: 0; right: 0; top: 12.6em; height: 3em;
    display: flex; align-items: center; justify-content: center; gap: 0.8em;
  }
  .label__brand-dot { width: 1.4em; height: 1.4em; background: var(--mark); }
  .label__brand-name { font-size: 1.7em; font-weight: 400; letter-spacing: 0.12em; color: var(--ink); }

  .label__name {
    position: absolute; left: 0; right: 0; top: 19.4em; height: 4.4em;
    display: flex; align-items: center; justify-content: center;
    font-weight: 600; font-size: 1em;
  }
  .label__name span { font-size: 3.6em; letter-spacing: 0.16em; line-height: 1; }

  .label__claims {
    position: absolute; left: 0; right: 0; top: 28.8em;
    list-style: none; text-align: center;
  }
  .label__claims li { height: 2.8em; line-height: 2.8em; white-space: nowrap; }
  .label__claims span {
    font-size: 1.45em; letter-spacing: 0.08em;
    color: var(--ink-soft); text-transform: uppercase;
  }
  .label__claims .label__lead span { color: var(--gold); font-weight: 600; }

  .label__count {
    position: absolute; left: 7.8em; top: 40.7em; width: 4.3em; height: 4.5em;
    background: var(--tint);
    display: flex; align-items: center; justify-content: center;
  }
  .label__count span { font-size: 2.4em; line-height: 1; }
  .label__unit {
    position: absolute; left: 12.6em; top: 43.6em;
    letter-spacing: 0.08em; color: var(--ink-soft); line-height: 1.3;
  }
  .label__unit span { display: block; font-size: 1.3em; }

  /* smaller jars in the back row */
  .jar--small { height: 47em; }
  .jar--small .jar__cap { height: 8em; }
  .jar--small .jar__body { top: 7.3em; }
  .jar--small .label__brand { top: 11.2em; }
  .jar--small .label__name { top: 17.4em; }
  .jar--small .label__name span { font-size: 3.4em; }
  .jar--small .label__tint-block { top: 13em; height: 13.5em; }
  .jar--small .label__muted-block { top: 23.5em; height: 10em; }
  .jar--small .label__claims { top: 26.2em; }
  .jar--small .label__claims li { height: 2.6em; line-height: 2.6em; }
  .jar--small .label__claims span { font-size: 1.2em; }
  .jar--small .label__count { top: 37em; width: 4em; height: 3.6em; }
  .jar--small .label__count span { font-size: 2em; }
  .jar--small .label__unit { top: 39.6em; }
  .jar--small .label__unit span { font-size: 1.1em; }

  .jar--glow   { left: 150px; top: 469px; font-size: 5.05px;
    --cap: var(--amber-cap); --mark: var(--amber-mark); --tint: var(--amber-tint); --muted: var(--amber-muted); }
  .jar--modig  { left: 939px; top: 486px; font-size: 3.5px;
    --cap: var(--teal-cap); --mark: var(--teal-mark); --tint: var(--teal-tint); --muted: var(--teal-muted); }
  .jar--vitala { left: 826px; top: 473px; font-size: 3.9px;
    --cap: var(--sky-cap); --mark: var(--sky-mark); --tint: var(--sky-tint); --muted: var(--sky-muted); }
  .jar--ljuva  { left: 695px; top: 459px; font-size: 4.5px;
    --cap: var(--plum-cap); --mark: var(--plum-mark); --tint: var(--plum-tint); --muted: var(--plum-muted); }
  .jar--skimra { left: 406px; top: 350px; font-size: 10px;
    --cap: var(--pink-cap); --mark: var(--pink-mark); --tint: var(--pink-tint); --muted: var(--pink-muted); }
</style>
</head>
<body>
<main class="lineup">

  <article class="jar jar--small jar--glow">
    <div class="jar__cap"></div>
    <div class="jar__body"></div>
    <div class="label__tint-block"></div>
    <div class="label__muted-block"></div>
    <div class="label__brand"><i class="label__brand-dot"></i><span class="label__brand-name">Ovela</span></div>
    <h2 class="label__name"><span>GLÖD</span></h2>
    <ul class="label__claims">
      <li class="label__lead"><span>Organic turmeric &amp; ginger</span></li>
      <li><span>Anti-inflammatory</span></li>
      <li><span>Antioxidant</span></li>
      <li><span>Promotes digestive health</span></li>
    </ul>
    <div class="label__count"><span>70</span></div>
    <p class="label__unit"><span>GUMMIES</span></p>
  </article>

  <article class="jar jar--small jar--modig">
    <div class="jar__cap"></div>
    <div class="jar__body"></div>
    <div class="label__tint-block"></div>
    <div class="label__muted-block"></div>
    <div class="label__brand"><i class="label__brand-dot"></i><span class="label__brand-name">Ovela</span></div>
    <h2 class="label__name"><span>MODIG</span></h2>
    <ul class="label__claims">
      <li class="label__lead"><span>Energizing multivitamin</span></li>
      <li class="label__lead"><span>For him</span></li>
      <li><span>13 vitamins</span></li>
      <li><span>9 minerals</span></li>
    </ul>
    <div class="label__count"><span>60</span></div>
    <p class="label__unit"><span>GUMMIES</span></p>
  </article>

  <article class="jar jar--small jar--vitala">
    <div class="jar__cap"></div>
    <div class="jar__body"></div>
    <div class="label__tint-block"></div>
    <div class="label__muted-block"></div>
    <div class="label__brand"><i class="label__brand-dot"></i><span class="label__brand-name">Ovela</span></div>
    <h2 class="label__name"><span>VITALA</span></h2>
    <ul class="label__claims">
      <li class="label__lead"><span>Energizing multivitamin</span></li>
      <li class="label__lead"><span>For her</span></li>
      <li><span>13 vitamins</span></li>
      <li><span>10 minerals</span></li>
    </ul>
    <div class="label__count"><span>60</span></div>
    <p class="label__unit"><span>GUMMIES</span></p>
  </article>

  <article class="jar jar--small jar--ljuva">
    <div class="jar__cap"></div>
    <div class="jar__body"></div>
    <div class="label__tint-block"></div>
    <div class="label__muted-block"></div>
    <div class="label__brand"><i class="label__brand-dot"></i><span class="label__brand-name">Ovela</span></div>
    <h2 class="label__name"><span>LJUVA</span></h2>
    <ul class="label__claims">
      <li class="label__lead"><span>Concentrated biotin</span></li>
      <li><span>Healthy hair</span></li>
      <li><span>Glowing skin</span></li>
      <li><span>Strong nails</span></li>
    </ul>
    <div class="label__count"><span>70</span></div>
    <p class="label__unit"><span>GUMMIES</span><span>SUGAR FREE</span></p>
  </article>

  <article class="jar jar--skimra">
    <div class="jar__cap"></div>
    <div class="jar__body"></div>
    <div class="label__tint-block"></div>
    <div class="label__muted-block"></div>
    <div class="label__brand"><i class="label__brand-dot"></i><span class="label__brand-name">Ovela</span></div>
    <h1 class="label__name"><span>SKIMRA</span></h1>
    <ul class="label__claims">
      <li class="label__lead"><span>Organic collagen</span></li>
      <li><span>Skin booster</span></li>
      <li><span>Joint booster</span></li>
      <li><span>Anti-aging</span></li>
    </ul>
    <div class="label__count"><span>70</span></div>
    <p class="label__unit"><span>GUMMIES</span></p>
  </article>

</main>
</body>
</html>
```